PREMIUM AGENCY High End Business Card - A+++ Designers Wanted

** DO NOT ATTEMPT TO CONTACT ME THROUGH SEARCHING ON GOOGLE OR EMAILING ME THROUGH MY WEBSITE **

I need a fresh, contemporary business card designed using the logo attached (VOLKRANE)

I have attached the font for VOLKRANE

It must have a premium look and feel. The business card size must be STANDARD size.

You can submit either/both VERTICAL or HORIZONTAL designs.

FRONT: It must have the following sample information on

Peter Dowle
Director Operations
Mobile +61 452 000 000
Email peterdowle@volkrane.example
www.volkrane.example

The REAR of the business card must have the words

IMAGINE SHAPE BEYOND

as part of the design, in the same font (NEXA) attached.

The words do not need to be in capitals, or on the same line, please design this as you see it best working.

ADDITIONAL INFORMATION
======================

The VOLKRANE logo must be on the front of the card

I want Ultraviolet printing on the final design, to enhance either the NAME of the person OR the VOLKRANE logo OR the words on the back of the card.

Target Market(s)

Agency, Advertising Agency, Creative, Designers

Industry/Entity Type

Media

Contact Information for Business Card

Design Agency, Contemporary, Premium look and feel, High Quality

Font styles to use
Serif
Sans Serif
Other font styles liked:
• ATTACHED TO PROJECT

Requirements
Must have
• BLACK & WHITE as the primary design, and if you feel there can be a highlighted colour, then this can be used.
• The Logo ICON attached is blue, this colour must not be changed.
• I have attached the partner brand VOLKRANE MEDIA incase you need to manipulate the original files.
• ** DO NOT ATTEMPT TO CONTACT ME THROUGH SEARCHING ON GOOGLE OR EMAILING ME THROUGH MY WEBSITE **
Nice to have
• Must be Premium. I have attached some sample designs, that I like that would be a good inspiration for where this can be taken.
• My favourite design is is the SNAPFRAME2-BUSINESSCARD-TEMPLATE
Should not have
• No funny or silly standard / off the shelf designs

```html
<!DOCTYPE html>
<html lang="en">
<head>
<meta charset="utf-8">
<title>Volkrane Media – Business Card</title>
<link rel="stylesheet" href="https://fonts.googleapis.com/css2?family=Montserrat:wght@300;400;700&display=swap">
<style>
  :root {
    --page: #e6e4e0;
    --card: #2a2a2b;
    --card-edge: #1c1c1d;
    --ink: #f2f2f2;
    --ink-soft: #d6d6d6;
    --accent: #29b6df;
    --accent-deep: #1a9cc6;
  }
  * { margin: 0; padding: 0; box-sizing: border-box; }
  html, body {
    width: 1200px; height: 780px; overflow: hidden;
    background: var(--page);
    font-family: "Montserrat", Arial, sans-serif;
  }
  .stage { position: relative; width: 1200px; height: 780px; }

  .card {
    position: absolute;
    background: radial-gradient(circle at 40% 30%, #323233 0%, var(--card) 55%, #232324 100%);
    box-shadow: 0 18px 40px rgba(0,0,0,.28), 0 2px 0 var(--card-edge);
    border-radius: 3px;
    overflow: hidden;
    color: var(--ink);
  }

  /* Front – vertical */
  .card-front {
    left: 130px; top: 110px; width: 320px; height: 560px;
    display: flex; flex-direction: column; align-items: center;
  }
  .brand-dot {
    width: 72px; height: 72px; border-radius: 50%;
    background: var(--accent);
    margin-top: 70px;
  }
  .brand-name {
    margin-top: 22px;
    font-weight: 400; font-size: 20px; letter-spacing: 3px;
    color: var(--ink);
  }
  .person { margin-top: 54px; text-align: center; }
  .person-name {
    font-weight: 700; font-size: 22px; letter-spacing: 1.5px;
    color: var(--accent); text-transform: uppercase;
  }
  .person-role {
    margin-top: 2px; font-weight: 400; font-size: 15px; letter-spacing: .8px;
    color: var(--ink);
  }
  .contact {
    margin-top: 28px; list-style: none; text-align: center;
    font-weight: 400; font-size: 13px; line-height: 1.75; letter-spacing: .6px;
    color: var(--ink-soft);
  }
  .edge-band {
    position: absolute; left: 0; right: 0; bottom: 0; height: 62px;
    background: linear-gradient(90deg, var(--accent-deep), var(--accent));
  }

  /* Back – horizontal */
  .card-back {
    left: 540px; top: 230px; width: 560px; height: 320px;
  }
  .back-brand {
    position: absolute; left: 40px; top: 110px;
    display: flex; align-items: center; gap: 16px;
  }
  .back-dot {
    width: 46px; height: 46px; border-radius: 50%;
    background: var(--accent);
  }
  .back-name {
    font-weight: 400; font-size: 36px; letter-spacing: 3px;
    color: var(--ink); white-space: nowrap;
  }
  .tagline {
    position: absolute; left: 102px; top: 172px;
    font-weight: 300; font-size: 15px; letter-spacing: 1.2px;
    color: var(--accent);
  }
</style>
</head>
<body>
<main class="stage">
  <section class="card card-front" aria-label="Business card front">
    <div class="brand-dot" aria-hidden="true"></div>
    <div class="brand-name">VOLKRANE MEDIA</div>
    <div class="person">
      <div class="person-name">Peter Dowle</div>
      <div class="person-role">Director Operations</div>
    </div>
    <ul class="contact">
      <li>+61 452 000 000</li>
      <li>peterdowle@volkrane.example</li>
      <li>www.volkrane.example</li>
    </ul>
    <div class="edge-band" aria-hidden="true"></div>
  </section>

  <section class="card card-back" aria-label="Business card back">
    <div class="back-brand">
      <div class="back-dot" aria-hidden="true"></div>
      <div class="back-name">VOLKRANE MEDIA</div>
    </div>
    <div class="tagline">IMAGINE SHAPE BEYOND</div>
  </section>
</main>
</body>
</html>
```